Business card design needed for Marbury Medical Practice

We need a new design for our growing medical practice. Our previous design used blue, white and black. I would like to have a design with a baby, child, adult and grandparent on it. We look after a wide range of patients from newborns to 100 year olds.

Industry/Entity Type

Medical

Contact Information for Business Card

Marbury Medical Practice
14 Dunmore Rd Lawson, NSW 2783
Ph 4820 3647 Fax 4913 2506
Dr Helen Voss Dr Andrea Pollard
Dr Wendy Trelawny Dr Janice Whitworth
Dr Tom Ashbrook Dr Neil Dunn-Foster
Open Mon- Fri 9-1, 2-5pm
Sat 9-12pm by appointment
web:www.marburymedix.com.au
email:marburymedix@mailzonex.com

```html
<!DOCTYPE html>
<html lang="en">
<head>
<meta charset="utf-8">
<title>Marbury Medical Practice – Business Card</title>
<link rel="stylesheet" href="https://fonts.googleapis.com/css2?family=Open+Sans:wght@700&family=EB+Garamond:wght@400;500&display=swap">
<style>
  :root {
    --backdrop: #2a2a2a;
    --card-white: #ffffff;
    --brand-red: #7d1518;
    --brand-red-deep: #5e0f11;
    --ink: #1c1c1c;
    --band-text: #f3e2e2;
    --icon-red: #8e1b1e;
    --silhouette: #1a1a1a;
  }
  * { margin: 0; padding: 0; box-sizing: border-box; }
  html, body { width: 1200px; height: 900px; overflow: hidden; background: var(--backdrop); }
  .canvas { position: relative; width: 1200px; height: 900px; }
  .card {
    position: absolute; left: 300px; width: 600px; height: 343px;
    background: var(--card-white); overflow: hidden;
    box-shadow: 0 10px 30px rgba(0,0,0,.55);
  }
  .card--front { top: 90px; }
  .card--back { top: 467px; }
  .card__band { position: absolute; inset: 0; width: 600px; height: 343px; }
  .serif { font-family: "EB Garamond", Georgia, serif; }

  .practice-name {
    position: absolute; left: 34px; top: 42px;
    font-family: "Open Sans", Arial, sans-serif; font-weight: 700;
    font-size: 30px; color: var(--ink); letter-spacing: .5px; white-space: nowrap;
  }
  .family-figures {
    position: absolute; left: 200px; top: 96px; width: 200px; height: 114px;
    background: linear-gradient(180deg, #444 0%, var(--silhouette) 100%);
    border-radius: 6px 6px 0 0; opacity: .9;
  }
  .card--back .family-figures { left: 205px; top: 92px; }

  .front-info {
    position: absolute; left: 0; right: 140px; top: 222px;
    text-align: center; color: var(--band-text); font-size: 19px; line-height: 1.25;
  }
  .front-info .web { display: inline-flex; align-items: center; gap: 6px; }

  .contact-row {
    position: absolute; top: 20px; right: 40px;
    display: flex; gap: 22px; font-size: 15px; color: var(--ink); align-items: center; white-space: nowrap;
  }
  .contact-row span, .email { display: inline-flex; align-items: center; gap: 6px; }
  .email { position: absolute; top: 44px; left: 246px; font-size: 15px; color: var(--ink); white-space: nowrap; }
  .icon { width: 16px; height: 14px; fill: var(--icon-red); }

  .doctors {
    position: absolute; left: 0; right: 0; top: 228px;
    text-align: center; color: var(--band-text); font-size: 20px; line-height: 1.2;
  }
  .dot { font-size: 12px; vertical-align: middle; margin: 0 4px; }
</style>
</head>
<body>
<main class="canvas">

  <section class="card card--front" aria-label="Card front">
    <svg class="card__band" viewBox="0 0 600 343" aria-hidden="true">
      <defs>
        <linearGradient id="bandFront" x1="0" y1="0" x2="0" y2="1">
          <stop offset="0" stop-color="#8a181b"/><stop offset="1" stop-color="#5e0f11"/>
        </linearGradient>
      </defs>
      <path d="M0 210 L430 210 L438 160 L452 172 L476 48 L494 160 L514 30 L534 140 L552 112 L600 112 L600 343 L0 343 Z"
            fill="url(#bandFront)" stroke="#111" stroke-width="2"/>
    </svg>
    <div class="practice-name">Marbury Medical Practice</div>
    <div class="family-figures" role="img" aria-label="Silhouettes of a baby, a child on a scooter, an adult and a grandparent with a cane"></div>
    <div class="front-info serif">
      <div class="web">
        <svg class="icon" viewBox="0 0 16 16" style="fill:var(--band-text)"><path d="M8 1a5 5 0 0 0-5 5c0 4 5 9 5 9s5-5 5-9a5 5 0 0 0-5-5zm0 7a2 2 0 1 1 0-4 2 2 0 0 1 0 4z"/></svg>
        www.marburymedix.com.au
      </div>
      <div>Open:</div>
      <div>Mon- Fri 9-1, 2-5pm</div>
      <div>Sat 9-12pm by appointment</div>
    </div>
  </section>

  <section class="card card--back" aria-label="Card back">
    <svg class="card__band" viewBox="0 0 600 343" aria-hidden="true">
      <defs>
        <linearGradient id="bandBack" x1="0" y1="0" x2="0" y2="1">
          <stop offset="0" stop-color="#8a181b"/><stop offset="1" stop-color="#5e0f11"/>
        </linearGradient>
      </defs>
      <path d="M0 210 L440 210 L446 150 L466 172 L488 50 L506 178 L524 78 L540 152 L556 130 L600 130 L600 343 L0 343 Z"
            fill="url(#bandBack)" stroke="#111" stroke-width="2"/>
    </svg>
    <div class="contact-row serif">
      <span><svg class="icon" viewBox="0 0 16 14"><path d="M1 5c2-3 12-3 14 0l-2 2-2-1V4H5v2L3 7zM3 8h10v5H3z"/></svg>4820 3647</span>
      <span><svg class="icon" viewBox="0 0 16 14"><path d="M4 1h8v3H4zM1 5h14v6h-3v2H4v-2H1zM5 9v3h6V9z"/></svg>4913 2506</span>
      <span><svg class="icon" viewBox="0 0 16 14"><path d="M8 0l8 7h-2v7h-4V9H6v5H2V7H0z"/></svg>14 Dunmore Rd Kellbrook NSW 2791</span>
    </div>
    <div class="email serif">
      <svg class="icon" viewBox="0 0 16 16"><circle cx="8" cy="8" r="7"/><text x="8" y="11.5" font-size="10" text-anchor="middle" fill="#fff" font-family="Arial, sans-serif">@</text></svg>
      marburymedix@mailzonex.com
    </div>
    <div class="family-figures" role="img" aria-label="Silhouettes of a baby, a child on a scooter, an adult and a grandparent with a cane"></div>
    <div class="doctors serif">
      <div>Dr Helen Voss <span class="dot">●</span> Dr Andrea Pollard</div>
      <div>Dr Wendy Trelawny <span class="dot">●</span> Dr Janice Whitworth</div>
      <div>Dr Tom Ashbrook <span class="dot">●</span> Dr Neil Dunn-Foster</div>
    </div>
  </section>

</main>
</body>
</html>
```